Lumo Tails

im a dog walker, pet sitter and dog groomer. I can look after all pets from once a day pop in feeds of cats to small holdings and exotics. have 10 years experience in the industry. I can look after peoples dogs for the day while they are out or for longer if on holiday. I walk dogs when people are at work so the dogs get to have fun too. I do house sitting so all your animals are looked after together. you have designed my business cards and I wanted the 'lumo tails' with the paw to be the same on the leaflets. I have spoken to brandlark and they have sent a pdf file of business card and said it can be cropped. please let me know if this cant be done
im also a qualified canine hydrotherapist

Target Market(s)

pet owners

Industry/Entity Type

Pet

Requirements
Must have
• my phone number 07835204617
• email lumotails@mailnest.co.uk
• area; Tunbridge wells, Sevenoaks and surrounding areas
• I want it almost done as bullet points with the main things being the dog walking and the pet sitting.
Nice to have
• cartoon animals like business card not the cartoons with big eyes

```html
<!DOCTYPE html>
<html lang="en">
<head>
<meta charset="utf-8">
<title>Lumo Tails – Dog Walker, Pet Sitter &amp; Dog Groomer</title>
<link rel="stylesheet" href="https://fonts.googleapis.com/css2?family=Montserrat:wght@700&family=Roboto+Condensed:wght@300&family=Cormorant+Garamond:wght@500&display=swap">
<style>
  :root {
    --purple: #7d5aa6;
    --purple-soft: #a98bc8;
    --lavender: #e6dcf0;
    --white: #ffffff;
    --ink: #2b2b2b;
    --teal: #2b9ad4;
    --grass: #6f9a3a;
    --grass-light: #a7c46a;
    --brown: #6b4230;
  }
  * { margin: 0; padding: 0; box-sizing: border-box; }
  html, body { width: 846px; height: 1200px; overflow: hidden; background: var(--white); }
  .leaflet {
    position: relative;
    width: 846px;
    height: 1200px;
    overflow: hidden;
    background: var(--white);
  }
  .backdrop {
    position: absolute;
    left: 0; top: 0;
    width: 846px; height: 836px;
    background:
      radial-gradient(ellipse 70% 60% at 50% 62%, rgba(255,255,255,0.95) 0%, rgba(255,255,255,0.6) 45%, rgba(255,255,255,0) 80%),
      linear-gradient(180deg, var(--purple-soft) 0%, #c2abd8 35%, var(--lavender) 70%, #f6f2fa 100%);
  }
  .headline {
    position: absolute;
    top: 28px; left: 0; width: 100%;
    text-align: center;
    font-family: 'Montserrat', sans-serif;
    font-weight: 700;
    font-size: 28px;
    letter-spacing: 0.5px;
    color: var(--white);
  }
  .hero {
    position: absolute;
    left: 132px; top: 88px;
    width: 582px; height: 384px;
    background:
      radial-gradient(ellipse 30% 55% at 60% 45%, var(--brown) 0%, rgba(107,66,48,0.85) 50%, rgba(107,66,48,0) 100%),
      linear-gradient(180deg, #3f5a2a 0%, var(--grass) 45%, var(--grass-light) 100%);
    box-shadow: 0 6px 14px rgba(0,0,0,0.25);
  }
  .services {
    position: absolute;
    left: 116px; top: 520px;
    list-style: none;
    font-family: 'Roboto Condensed', sans-serif;
    font-weight: 300;
    font-size: 27px;
    line-height: 38px;
    color: var(--ink);
  }
  .services li { position: relative; padding-left: 28px; }
  .services li::before {
    content: "";
    position: absolute;
    left: 2px; top: 14px;
    width: 12px; height: 12px;
    border-radius: 50%;
    background: var(--purple);
  }
  .area {
    position: absolute;
    top: 818px; left: 0; width: 100%;
    text-align: center;
    font-family: 'Cormorant Garamond', serif;
    font-weight: 500;
    font-size: 30px;
    color: var(--teal);
  }
  .brand {
    position: absolute;
    top: 920px; left: 0; width: 100%;
    display: flex;
    justify-content: center;
    align-items: center;
    gap: 26px;
  }
  .brand-dot {
    width: 120px; height: 120px;
    border-radius: 50%;
    background: #e8b84a;
  }
  .brand-name {
    font-family: 'Cormorant Garamond', serif;
    font-weight: 500;
    font-size: 64px;
    color: var(--purple);
  }
  .tagline {
    position: absolute;
    top: 1052px; left: 0; width: 100%;
    text-align: center;
    font-family: 'Cormorant Garamond', serif;
    font-weight: 500;
    font-size: 30px;
    color: var(--teal);
  }
  .contact-bar {
    position: absolute;
    left: 0; top: 1124px;
    width: 846px; height: 76px;
    background: var(--purple);
    display: flex;
    justify-content: center;
    align-items: center;
    font-family: 'Roboto Condensed', sans-serif;
    font-weight: 300;
    font-size: 34px;
    color: var(--white);
    gap: 16px;
  }
</style>
</head>
<body>
<main class="leaflet">
  <div class="backdrop"></div>
  <h1 class="headline">DOG WALKER, PET SITTER &amp; DOG GROOMER</h1>
  <div class="hero" role="img" aria-label="Cartoon illustration of a large brown dog sitting on grass with a cat, a hen, a chick, a lizard and a rabbit"></div>
  <ul class="services">
    <li>Dog walker, pet sitter &amp; dog groomer</li>
    <li>Pet / House sitting - can pop in to feed<br>your pets or small holdings and exotics</li>
    <li>10 years experience</li>
    <li>Will sit pets a portion or the day, all day or all week!</li>
    <li>Ensure pets get exercise and fun</li>
    <li>Qualified canine hydrotherapist</li>
  </ul>
  <p class="area">Tunbridge Wells, Sevenoaks and surrounding areas</p>
  <div class="brand">
    <span class="brand-dot"></span>
    <span class="brand-name">Lumo Tails</span>
  </div>
  <p class="tagline">10 years experience in animal industry</p>
  <footer class="contact-bar">
    <span class="phone">07835204617</span>
    <span class="divider">|</span>
    <span class="email">email lumotails@mailnest.co.uk</span>
  </footer>
</main>
</body>
</html>
```